Resume build

I need someone to develop a resume for me. This needs to include a stylized template as well as improving the content of my existing resume.
Updates

All content generated. Just need resume to be formatted and stylized a few different options. With offer a few different head shots to go into it as well. Final versions to be in PDF.

Target Market(s)

this is not for finding a job but is for presenting to clients on who I am and why I'm the qualified candidate to perform their work.

Industry/Entity Type

Marine

Colors
0054AA
0677BA
7BADD7
CADEEF
E8F1F8

Requirements
Must have
• must be in PDF and have a location to add a picture later in the top corner

```html
<!DOCTYPE html>
<html lang="en">
<head>
<meta charset="utf-8">
<title>Rowan Tallis – Resume</title>
<link href="https://fonts.googleapis.com/css2?family=Montserrat:wght@400;500;600;700;800&display=swap" rel="stylesheet">
<style>
  :root {
    --backdrop: #f3f3f3;
    --paper: #ffffff;
    --navy: #073789;
    --navy-dark: #052c70;
    --navy-mid: #0a3f96;
    --blue: #0054AA;
    --bar: #0677BA;
    --sky: #7BADD7;
    --column: #CADEEF;
    --track: #E8F1F8;
    --ink: #111111;
    --ink-soft: #222222;
    --photo: #8a8d91;
  }
  * { box-sizing: border-box; margin: 0; padding: 0; }
  html, body { width: 1200px; height: 840px; overflow: hidden; }
  body {
    background: var(--backdrop);
    font-family: "Montserrat", Arial, sans-serif;
    color: var(--ink);
    position: relative;
  }
  .resume {
    position: absolute;
    left: 317px; top: 20px;
    width: 566px; height: 800px;
    background: var(--paper);
    box-shadow: 0 6px 24px rgba(0,0,0,.12);
    overflow: hidden;
  }
  .sidebar {
    position: absolute;
    left: 31px; top: 0;
    width: 211px; height: 100%;
    background: var(--column);
  }
  .header-band {
    position: absolute;
    left: 0; top: 74px;
    width: 566px; height: 110px;
  }
  .portrait {
    position: absolute;
    left: 63px; top: 53px;
    width: 152px; height: 152px;
    border-radius: 50%;
    border: 3px solid var(--navy);
    background: radial-gradient(circle at 50% 40%, #f4f4f4 0 60%, #e6e6e6 100%);
    display: flex; align-items: center; justify-content: center;
  }
  .portrait-fill {
    width: 100px; height: 118px;
    margin-top: 30px;
    border-radius: 50px 50px 10px 10px;
    background: var(--photo);
  }
  .name-block {
    position: absolute;
    left: 262px; top: 96px;
    color: #fff;
  }
  .name {
    font-weight: 800;
    font-size: 35px;
    letter-spacing: .5px;
    line-height: 1;
  }
  .role-title {
    margin-top: 9px;
    margin-left: 4px;
    font-size: 12.5px;
    font-weight: 400;
  }

  /* sidebar content */
  .about-title {
    position: absolute; left: 31px; top: 213px; width: 211px;
    text-align: center; font-size: 15.5px; font-weight: 400;
  }
  .about-text {
    position: absolute; left: 66px; top: 240px; width: 140px;
    text-align: center; font-size: 8.3px; line-height: 12px;
  }
  .contact-list { position: absolute; left: 66px; top: 331px; list-style: none; }
  .contact-list li {
    display: flex; align-items: center; gap: 7px;
    font-size: 8.5px; height: 18px; margin-bottom: 12px;
  }
  .contact-list svg { width: 17px; height: 17px; flex: none; }
  .outline-pill {
    position: absolute; left: 59px; width: 160px; height: 25px;
    border: 1.5px solid var(--navy); border-radius: 13px;
    text-align: center; font-size: 11px; line-height: 22px;
  }
  .bullet-list {
    position: absolute; left: 82px;
    font-size: 10.5px; line-height: 19.4px;
    list-style: none;
  }
  .bullet-list li::before {
    content: ""; display: inline-block;
    width: 4px; height: 4px; border-radius: 50%;
    background: var(--ink); margin-right: 9px; vertical-align: middle;
    position: relative; top: -1px;
  }

  /* main column */
  .section-pill {
    position: absolute; left: 250px; width: 141px; height: 22px;
    background: var(--navy); color: #fff; border-radius: 11px;
    text-align: center; font-size: 11px; line-height: 22px;
  }
  .entry { position: absolute; left: 255px; width: 270px; }
  .entry-head { font-size: 9.8px; font-weight: 600; line-height: 14px; }
  .entry-body { margin-top: 3px; font-size: 8.6px; line-height: 13px; }
  .edu-name { font-size: 9.8px; font-weight: 600; line-height: 13px; }
  .edu-detail { font-size: 8.8px; line-height: 12.5px; }
  .skill {
    position: absolute; left: 256px; width: 240px;
    display: flex; align-items: center; font-size: 9px;
  }
  .skill-label { width: 123px; }
  .skill-track {
    width: 60px; height: 4px; border-radius: 2px;
    background: var(--track); position: relative;
  }
  .skill-level {
    position: absolute; left: 0; top: 0; height: 4px; border-radius: 2px;
    background: var(--bar);
  }
  .skill-value { margin-left: 4px; font-size: 13px; color: var(--blue); }
</style>
</head>
<body>
<main class="resume">
  <div class="sidebar"></div>

  <svg class="header-band" viewBox="0 0 566 110" aria-hidden="true">
    <rect width="566" height="110" fill="var(--navy)"/>
    <polygon points="0,0 50,0 10,110 0,110" fill="var(--navy-dark)"/>
    <polygon points="50,0 270,0 232,110 10,110" fill="var(--navy-mid)"/>
    <polygon points="50,0 70,0 30,110 10,110" fill="var(--navy-dark)" opacity=".5"/>
  </svg>

  <div class="portrait">
    <div class="portrait-fill" role="img" aria-label="Headshot photo placeholder"></div>
  </div>

  <div class="name-block">
    <h1 class="name">ROWAN TALLIS</h1>
    <p class="role-title">Marine Project Operations Manager</p>
  </div>

  <h2 class="about-title">About Me</h2>
  <p class="about-text">Lorem ipsum dolor sit amet, consectetur adipiscing elit. Vestibulum sit amet quam rhoncus, egestas dui eget, malesuada justo. Ut aliquam augue dui.</p>

  <ul class="contact-list">
    <li>
      <svg viewBox="0 0 20 20"><circle cx="10" cy="10" r="10" fill="var(--ink)"/><path d="M6.5 5.5l2 0 .8 2.3-1.2 1c.6 1.3 1.6 2.3 2.9 2.9l1-1.2 2.3.8 0 2c0 .6-.5 1-1 1C9.4 14.3 5.7 10.6 5.5 6.5c0-.5.4-1 1-1z" fill="#fff"/></svg>
      +61 2 5550 1847
    </li>
    <li>
      <svg viewBox="0 0 20 20"><circle cx="10" cy="10" r="10" fill="var(--ink)"/><rect x="5" y="6.5" width="10" height="7" rx="1" fill="#fff"/><path d="M5.5 7l4.5 3.5L14.5 7" stroke="var(--ink)" stroke-width="1.2" fill="none"/></svg>
      hello@tallismarine.com
    </li>
    <li>
      <svg viewBox="0 0 20 20"><circle cx="10" cy="10" r="10" fill="var(--ink)"/><path d="M10 4.5a3.6 3.6 0 0 1 3.6 3.6c0 2.6-3.6 6.9-3.6 6.9S6.4 10.7 6.4 8.1A3.6 3.6 0 0 1 10 4.5z" fill="#fff"/><circle cx="10" cy="8.1" r="1.4" fill="var(--ink)"/></svg>
      48 Harbour Rd., Port Kembla
    </li>
  </ul>

  <div class="outline-pill" style="top:434px">Language</div>
  <ul class="bullet-list" style="top:469px">
    <li>English</li>
    <li>Germany (basic)</li>
    <li>Spain (basic)</li>
  </ul>

  <div class="outline-pill" style="top:538px">Expertise</div>
  <ul class="bullet-list" style="top:570px;left:80px">
    <li>Management Skills</li>
    <li>Creativity</li>
    <li>Digital Marketing</li>
    <li>Negotiation</li>
    <li>Critical Thinking</li>
    <li>Leadership</li>
  </ul>

  <div class="section-pill" style="top:207px">Experience</div>
  <article class="entry" style="top:243px">
    <p class="entry-head">Keelhaven Industries<br>Sydney - Australia<br>2020 - 2022</p>
    <p class="entry-body">Lorem ipsum dolor sit amet, consectetur adipiscing elit. Vestibulum sit amet quam rhoncus, egestas dui eget, malesuada justo. Ut aliquam augue.</p>
  </article>
  <article class="entry" style="top:339px">
    <p class="entry-head">Saltmere Inc.<br>Sydney - Australia<br>2016 - 2020</p>
    <p class="entry-body">Lorem ipsum dolor sit amet, consectetur adipiscing elit. Vestibulum sit amet quam rhoncus, egestas dui eget, malesuada justo. Ut aliquam augue.</p>
  </article>
  <article class="entry" style="top:435px">
    <p class="entry-head">Studio Brinewell<br>Sydney - Australia<br>2010 - 2015</p>
    <p class="entry-body">Lorem ipsum dolor sit amet, consectetur adipiscing elit. Vestibulum sit amet quam rhoncus, egestas dui eget, malesuada justo. Ut aliquam augue.</p>
  </article>

  <div class="section-pill" style="top:538px">Education</div>
  <article class="entry" style="top:574px;left:256px">
    <p class="edu-name">Coastline University</p>
    <p class="edu-detail">Bachelor of Business Management<br>2014 - 2023</p>
  </article>
  <article class="entry" style="top:623px">
    <p class="edu-name">Coastline University</p>
    <p class="edu-detail">Master of Business Management<br>2014 - 2018</p>
  </article>

  <div class="section-pill" style="top:673px;height:23px;line-height:23px">Skills Summary</div>
  <div class="skill" style="top:706px">
    <span class="skill-label">Design Process</span>
    <span class="skill-track"><span class="skill-level" style="width:78%"></span></span>
    <span class="skill-value">78 %</span>
  </div>
  <div class="skill" style="top:727px">
    <span class="skill-label">Project Management</span>
    <span class="skill-track"><span class="skill-level" style="width:81%"></span></span>
    <span class="skill-value">81 %</span>
  </div>
</main>
</body>
</html>
```